Harlow Painting Postcard

Harlow Painting
Interior & Exterior Custom Painting
Tamber Hollow Club Home Owner
Insurance Work
Deck Staining
Licensed and Insured
Free Estimates

I included at bid for a person named Lorena Whitsby. I did that only so you could use the logo and company name off of the letter head. I do not want Lorena's info and job details on the postcard. Thank you.

```html
<!DOCTYPE html>
<html lang="en">
<head>
<meta charset="utf-8">
<title>Harlow Painting Postcard</title>
<link href="https://fonts.googleapis.com/css2?family=Open+Sans:wght@400;600;700&family=Tinos:wght@400;700&display=swap" rel="stylesheet">
<style>
  :root {
    --teal-deep: #0f4556;
    --teal: #1f6f86;
    --teal-light: #4aa3bb;
    --white: #ffffff;
    --ink: #1a1a1a;
    --ribbon: #c8161d;
    --check: #2a7fc0;
    --label-pink: #f6c6c9;
    --gold: #b58a3c;
    --gold-light: #e2c27a;
    --rule: #c9c9c9;
  }
  * { margin: 0; padding: 0; box-sizing: border-box; }
  html, body { width: 740px; height: 1200px; overflow: hidden; background: var(--white); }
  .canvas { position: relative; width: 740px; height: 1200px; }

  /* Front */
  .front { position: absolute; left: 0; top: 0; width: 740px; height: 572px; overflow: hidden; background: var(--teal); }
  .house-photo { position: absolute; left: 0; top: 100px; width: 740px; height: 390px;
    background: linear-gradient(180deg, #9cc3dd 0%, #7a8a7c 38%, #4f5a55 60%, #3f6a3a 85%, #2f5a2c 100%); }
  .front-bands { position: absolute; inset: 0; }
  .front-name { position: absolute; left: 22px; top: 76px; width: 350px; text-align: center;
    font-family: "Tinos", serif; font-weight: 700; font-size: 34px; color: var(--white);
    text-transform: uppercase; letter-spacing: 0.5px; }
  .services { position: absolute; left: 19px; top: 204px; list-style: none; }
  .services li { display: flex; align-items: center; justify-content: space-between;
    width: 282px; height: 38px; margin-bottom: 6px; padding-left: 14px; padding-right: 6px;
    background: rgba(12, 35, 45, 0.82); color: var(--white);
    font-family: "Open Sans", sans-serif; font-size: 21px; }
  .services svg { width: 28px; height: 28px; }
  .ribbon { position: absolute; left: -60px; top: 448px; width: 330px; height: 88px;
    transform: rotate(40deg); transform-origin: center; background: var(--ribbon);
    color: var(--white); font-family: "Open Sans", sans-serif; font-weight: 700;
    font-size: 22px; line-height: 28px; text-align: center; padding-top: 16px; }
  .tagline { position: absolute; right: 14px; top: 450px; text-align: right;
    font-family: "Tinos", serif; font-weight: 700; font-size: 27px; line-height: 36px; color: var(--white); }
  .phone { position: absolute; right: 12px; top: 520px; font-family: "Open Sans", sans-serif;
    font-weight: 600; font-size: 42px; color: var(--white); }

  /* Back */
  .back { position: absolute; left: 0; top: 593px; width: 740px; height: 607px;
    border: 1px solid var(--rule); background: var(--white); }
  .address-zone { position: absolute; inset: 0; }
  .back-name { position: absolute; left: 14px; top: 120px; width: 320px; text-align: center;
    font-family: "Tinos", serif; font-weight: 700; font-size: 30px; color: var(--ink);
    text-transform: uppercase; border-bottom: 2px solid var(--ink); padding-bottom: 4px; }
  .contact { position: absolute; left: 10px; top: 176px; width: 320px; text-align: center;
    font-family: "Tinos", serif; color: var(--ink); }
  .contact .person { font-weight: 700; font-size: 34px; line-height: 42px; }
  .contact .lines { margin-top: 24px; font-weight: 700; font-size: 20px; line-height: 30px; }
  .seal { position: absolute; left: 88px; top: 350px; width: 164px; height: 164px; }
  .return-address { position: absolute; left: 355px; top: 52px; font-family: "Tinos", serif;
    font-size: 22px; line-height: 30px; color: var(--ink); }
</style>
</head>
<body>
<main class="canvas">
  <section class="front">
    <div class="house-photo" role="img" aria-label="Photo of a freshly painted two-storey grey house with white trim, green shrubs and trees"></div>
    <svg class="front-bands" width="740" height="572" viewBox="0 0 740 572" aria-hidden="true">
      <defs>
        <linearGradient id="headerFill" x1="0" y1="0" x2="1" y2="0">
          <stop offset="0" stop-color="#0f4556"/>
          <stop offset="1" stop-color="#2b7f98"/>
        </linearGradient>
        <linearGradient id="footerFill" x1="0" y1="0" x2="0" y2="1">
          <stop offset="0" stop-color="#2b7f98"/>
          <stop offset="1" stop-color="#0f4556"/>
        </linearGradient>
      </defs>
      <path d="M0 0 H740 V60 C560 90 420 150 250 140 C150 134 60 118 0 112 Z" fill="url(#headerFill)"/>
      <path d="M0 112 C60 118 150 134 250 140 C420 150 560 90 740 60 V78 C560 108 420 166 250 156 C150 150 60 134 0 128 Z" fill="#d8e6ea" opacity="0.75"/>
      <path d="M0 520 C220 500 480 470 740 430 V572 H0 Z" fill="url(#footerFill)"/>
      <path d="M0 510 C220 490 480 460 740 420 V432 C480 472 220 502 0 522 Z" fill="#d8e6ea" opacity="0.7"/>
    </svg>
    <div class="front-name">Harlow Painting</div>
    <ul class="services">
      <li>Insurance Work<svg viewBox="0 0 28 28"><rect x="1" y="1" width="26" height="26" rx="3" fill="var(--check)" stroke="#fff" stroke-width="2"/><path d="M7 14 L12 19 L21 8" fill="none" stroke="#fff" stroke-width="3"/></svg></li>
      <li>Deck Staining<svg viewBox="0 0 28 28"><rect x="1" y="1" width="26" height="26" rx="3" fill="var(--check)" stroke="#fff" stroke-width="2"/><path d="M7 14 L12 19 L21 8" fill="none" stroke="#fff" stroke-width="3"/></svg></li>
      <li>Licensed and Insured<svg viewBox="0 0 28 28"><rect x="1" y="1" width="26" height="26" rx="3" fill="var(--check)" stroke="#fff" stroke-width="2"/><path d="M7 14 L12 19 L21 8" fill="none" stroke="#fff" stroke-width="3"/></svg></li>
      <li>Free Estimates<svg viewBox="0 0 28 28"><rect x="1" y="1" width="26" height="26" rx="3" fill="var(--check)" stroke="#fff" stroke-width="2"/><path d="M7 14 L12 19 L21 8" fill="none" stroke="#fff" stroke-width="3"/></svg></li>
    </ul>
    <div class="ribbon">Tamber Hollow Club<br>Home Owner</div>
    <p class="tagline">Interior &amp; Exterior<br>Custom Painting</p>
    <p class="phone">(555) 214-7730</p>
  </section>

  <section class="back">
    <svg class="address-zone" width="740" height="607" viewBox="0 0 740 607" aria-hidden="true">
      <rect x="569" y="3" width="170" height="201" fill="var(--label-pink)"/>
      <path d="M362 223 H739 V606 H88 V517 H362 Z" fill="var(--label-pink)"/>
    </svg>
    <div class="back-name">Harlow Painting</div>
    <div class="contact">
      <p class="person">Marcus Delane<br>Owner</p>
      <p class="lines">(555) 214-7730 Office<br>(555) 388-0192 Mobile</p>
    </div>
    <svg class="seal" viewBox="0 0 164 164" aria-hidden="true">
      <defs>
        <radialGradient id="sealFill" cx="0.4" cy="0.35" r="0.7">
          <stop offset="0" stop-color="var(--gold-light)"/>
          <stop offset="1" stop-color="var(--gold)"/>
        </radialGradient>
      </defs>
      <circle cx="82" cy="82" r="78" fill="url(#sealFill)"/>
    </svg>
    <p class="return-address">41 Tamber Hollow Lane<br>Coastal Bay, SC<br>29900</p>
  </section>
</main>
</body>
</html>
```